Business card for Velvet & Lark weddings and events management company
Velvet & Lark
Business card for Velvet & Lark weddings and events management company - Events
Creative Brief
Modern
Nargiza Huseynova
General Manager
17 Samad Str. AZ 1014, Baku, Azerbaijan
nargiza.huseynova@velvetlark-example.az
www.velvetlark-example.az
In addition to english version, be ready to provide azerbaijani version with little changes in titles as seen below: Name: Nərgizə Hüseynova Title: Müdir Address: Samad küç., 17 AZ1014, Bakı, Azərbaycan Slogan on the back: Sevindirməklə sevinirik! (as seen on azerbaijani version of logo, using only capital letters)
HAPPY TO MAKE YOU HAPPY! SEVİNDİRMƏKLƏ SEVİNİRİK! (on azerbaijani version) for this option, you can provide a different font as well, something maybe handwritten and more friendly. (Original font is Trajan Pro)
tulipwanderer tulipwanderer

```html
<!DOCTYPE html>
<html lang="en">
<head>
<meta charset="utf-8">
<title>Velvet &amp; Lark — Business Card</title>
<link rel="stylesheet" href="https://fonts.googleapis.com/css2?family=Cinzel:wght@400;600&family=Montserrat:wght@400;500&display=swap">
<style>
  :root {
    --bg: #d9d6d3;
    --ink: #111111;
    --paper: #ffffff;
    --silver: #a7a7a7;
    --silver-light: #cfcfcf;
    --muted: #555555;
  }
  * { box-sizing: border-box; margin: 0; padding: 0; }
  html, body { width: 1200px; height: 803px; overflow: hidden; }
  body {
    background: var(--bg);
    font-family: "Montserrat", Arial, sans-serif;
    position: relative;
  }
  .card {
    position: absolute;
    top: 253px;
    width: 520px;
    height: 297px;
    border-radius: 4px;
    overflow: hidden;
    box-shadow: 0 10px 24px rgba(0,0,0,0.18);
    background: var(--ink);
  }
  .card--front { left: 50px; }
  .card--back { left: 630px; }
  .card__shapes { position: absolute; inset: 0; width: 100%; height: 100%; }

  .brand {
    position: absolute; left: 52px; top: 38px;
    display: flex; align-items: center; gap: 14px;
  }
  .brand__dot { width: 40px; height: 40px; border-radius: 50%; background: var(--ink); }
  .brand__name {
    font-family: "Cinzel", "Times New Roman", serif;
    font-size: 30px; font-weight: 400; color: var(--ink); letter-spacing: 1px;
  }
  .brand__tagline {
    position: absolute; left: 106px; top: 86px;
    font-size: 8px; letter-spacing: 3px; color: var(--muted);
  }

  .contact {
    position: absolute; color: var(--paper); font-size: 11px; line-height: 1.45;
    display: flex; gap: 10px; align-items: flex-start;
  }
  .contact svg { flex: none; margin-top: 2px; }
  .contact--phone { left: 26px; top: 182px; }
  .contact--address { left: 26px; top: 226px; }
  .contact--web {
    right: 28px; top: 183px; color: var(--ink); font-weight: 500; font-size: 12px;
  }
  .contact--email { right: 26px; top: 258px; font-size: 11px; align-items: center; }

  .holder {
    position: absolute; right: 30px; top: 28px; text-align: right; color: var(--paper);
  }
  .holder__name { font-size: 17px; letter-spacing: 2px; text-transform: uppercase; }
  .holder__title { font-size: 11px; color: var(--silver-light); margin-top: 3px; }

  .slogan {
    position: absolute; left: 170px; top: 128px; width: 150px;
    text-align: center; color: var(--ink);
    font-family: "Cinzel", "Times New Roman", serif;
    font-size: 13px; font-weight: 600; line-height: 1.5; letter-spacing: 1px;
  }
</style>
</head>
<body>

  <section class="card card--front" aria-label="Business card, front">
    <svg class="card__shapes" viewBox="0 0 520 297" aria-hidden="true">
      <rect width="520" height="297" fill="var(--ink)"/>
      <path d="M0 0H520V150H250C232 150 228 138 212 138H0Z" fill="var(--paper)"/>
      <path d="M0 0H44L0 40Z" fill="var(--silver)"/>
      <path d="M0 138H212C228 138 232 150 250 150H520V162H0Z" fill="var(--silver)"/>
      <path d="M240 162H520V212H262C248 212 240 204 240 190Z" fill="var(--silver-light)"/>
      <path d="M470 0H520V30Z" fill="var(--silver)"/>
    </svg>

    <div class="brand">
      <span class="brand__dot"></span>
      <span class="brand__name">VELVET &amp; LARK</span>
    </div>
    <div class="brand__tagline">WEDDINGS &amp; EVENTS</div>

    <div class="contact contact--phone">
      <svg width="12" height="14" viewBox="0 0 12 14"><path d="M3 0L0 2C0 8 4 14 10 14L12 11L9 9L7 10C5 9 3 7 3 5L4 3Z" fill="var(--paper)"/></svg>
      <div>012 555 0147<br>012 555 0189</div>
    </div>
    <div class="contact contact--address">
      <svg width="14" height="13" viewBox="0 0 14 13"><path d="M7 0L14 6H12V13H8V9H6V13H2V6H0Z" fill="var(--paper)"/></svg>
      <div>17 Samad Str. AZ 1014<br>Baku, Azerbaijan</div>
    </div>
    <div class="contact contact--web">www.velvetlark-example.az</div>
    <div class="contact contact--email">
      <svg width="18" height="12" viewBox="0 0 18 12"><rect x="0.5" y="0.5" width="17" height="11" fill="none" stroke="var(--paper)"/><path d="M0.5 0.5L9 7L17.5 0.5" fill="none" stroke="var(--paper)"/></svg>
      <div>nargiza.huseynova@velvetlark-example.az</div>
    </div>
  </section>

  <section class="card card--back" aria-label="Business card, back">
    <svg class="card__shapes" viewBox="0 0 520 297" aria-hidden="true">
      <rect width="520" height="297" fill="var(--ink)"/>
      <path d="M150 297V120C150 96 166 84 190 84H300C324 84 340 96 340 120V297Z" fill="var(--silver)"/>
      <path d="M170 260V128C170 112 180 104 196 104H294C310 104 320 112 320 128V200C320 220 308 230 290 238L250 256C230 265 210 268 190 268C178 268 170 266 170 260Z" fill="var(--paper)"/>
      <path d="M0 297V250L120 297Z" fill="var(--silver)"/>
    </svg>
    <div class="holder">
      <div class="holder__name">Nargiza Huseynova</div>
      <div class="holder__title">General Manager</div>
    </div>
    <div class="slogan">HAPPY TO MAKE<br>YOU HAPPY!</div>
  </section>

</body>
</html>
```